Company or website name
- Haverford & Quist LLP
- Links to the website
- haverfordquist.com
- Describe your company and organization and target audience
- lawyers and clients in the need of lawyer for defective products etc
- The design should have the following
- yes
- Other Facts

```html
<!DOCTYPE html>
<html lang="en">
<head>
<meta charset="utf-8">
<title>Haverford &amp; Quist LLP</title>
<link rel="stylesheet" href="https://fonts.googleapis.com/css2?family=Lato:ital,wght@0,400;0,700;0,900;1,400;1,700&display=swap">
<style>
:root{
  --navy:#0d2a7a;
  --navy-deep:#0a1f5e;
  --royal:#1c3f9e;
  --ink:#3c3c3c;
  --text:#4a4a4a;
  --muted:#777;
  --white:#ffffff;
  --page:#f3f3f3;
  --sky-top:#c9d7ea;
  --sky-bottom:#5f82bd;
  --nav-top:#5a5a5a;
  --nav-bottom:#2f2f2f;
  --card:#d8dee8;
  --footer-text:#c7d0ea;
}
*{box-sizing:border-box;margin:0;padding:0}
html,body{width:1117px;height:1200px;overflow:hidden}
body{position:relative;font-family:"Lato",sans-serif;color:var(--text);background:var(--page)}
.abs{position:absolute}

.topbar{left:0;top:0;width:1117px;height:30px;background:var(--navy)}
.topbar .date{left:153px;top:10px;font-size:9px;color:var(--white);font-weight:700}
.topbar .util{right:147px;top:10px;font-size:9px;color:var(--white);font-weight:700;display:flex;gap:9px}
.topbar .util span.sep{opacity:.7;font-weight:400}

.masthead{left:0;top:30px;width:1117px;height:117px;background:linear-gradient(#f5f5f5,#e6e6e6)}
.brand{left:156px;top:67px;font-size:19px;font-weight:700;color:var(--navy);letter-spacing:.3px}
.callus{right:149px;top:72px;font-size:12px;color:var(--ink)}
.callus b{color:var(--navy)}

.sky{left:0;top:147px;width:1117px;height:318px;background:linear-gradient(var(--sky-top),var(--sky-bottom))}

.nav{left:153px;top:123px;width:817px;height:47px;background:linear-gradient(var(--nav-top),var(--nav-bottom));display:flex;border-radius:2px 2px 0 0}
.nav a{display:flex;align-items:center;justify-content:center;color:var(--white);font-size:13px;text-decoration:none;border-right:1px solid #777;height:100%}
.nav a.active{background:linear-gradient(var(--royal),var(--navy));font-weight:700}
.search{left:793px;top:132px;width:169px;height:27px;background:var(--white);border-radius:2px}
.search svg{position:absolute;right:7px;top:6px}

.hero{left:153px;top:170px;width:817px;height:295px;background:linear-gradient(180deg,#d6dce3 0%,#b7c1cb 45%,#dfe4ea 70%,#c3ccd5 100%)}
.hero-person{left:557px;top:170px;width:270px;height:295px;background:linear-gradient(180deg,#c9ccd2 0%,#2b2f38 55%,#1e222a 100%);border-radius:110px 110px 0 0}
.hero-panel{left:223px;top:228px;width:328px;height:171px;background:rgba(240,242,245,.82)}
.hero-panel h1{position:absolute;left:23px;top:15px;font-size:25px;font-weight:400;color:var(--ink);letter-spacing:.2px}
.hero-panel h1 b{color:var(--navy);font-weight:900}
.hero-panel .rule{position:absolute;left:23px;top:53px;width:276px;height:1px;background:var(--navy)}
.hero-panel p{position:absolute;left:23px;top:66px;width:275px;font-size:11.5px;line-height:15px;color:var(--ink)}
.btn{display:flex;align-items:center;justify-content:center;color:var(--white);font-size:9px;font-weight:700;letter-spacing:1px;border-radius:2px}
.btn.blue{background:linear-gradient(var(--royal),var(--navy-deep))}
.btn.dark{background:linear-gradient(#5a5a5a,#2b2b2b)}
.hero-panel .btn{position:absolute;left:24px;top:119px;width:146px;height:27px}
.arrow{width:35px;height:35px;border-radius:50%;border:1px solid rgba(255,255,255,.6);background:rgba(255,255,255,.15)}

.about-h{left:153px;top:501px;font-size:16px;color:var(--ink);display:flex;gap:14px;align-items:baseline}
.about-h b{font-size:14px;color:var(--navy)}
.about-p{left:153px;width:538px;font-size:9.6px;line-height:16px;color:var(--text)}
.know{left:600px;top:631px;width:90px;text-align:right;font-size:10px;font-style:italic;font-weight:700;color:var(--navy)}

.cases{left:709px;top:496px;width:261px;height:159px;background:var(--white);border:1px solid #dcdcdc;border-radius:3px}
.cases h2{position:absolute;left:0;top:10px;width:100%;text-align:center;font-size:15px;font-weight:700;color:var(--ink)}
.cases h2 span{color:var(--navy)}
.cases .rule{position:absolute;left:17px;top:34px;width:222px;height:1px;background:#e3e3e3}
.cases p{position:absolute;left:16px;width:220px;font-size:8px;line-height:14px;font-style:italic;color:var(--navy)}
.cases .track{position:absolute;left:240px;top:53px;width:1px;height:90px;background:#ccc}
.cases .thumb{position:absolute;left:239px;top:69px;width:3px;height:30px;background:var(--navy)}

.card{top:686px;width:261px;height:213px;background:linear-gradient(#e9ecf1,var(--card));border:1px solid #c6ccd6;border-radius:3px}
.card .head{height:36px;display:flex;align-items:center;justify-content:center;color:var(--white);font-size:10.5px;font-weight:700;border-radius:3px 3px 0 0}
.card .head.blue{background:linear-gradient(var(--royal),var(--navy-deep))}
.card .head.dark{background:linear-gradient(#666,#3a3a3a)}
.card .photo{position:absolute;left:12px;top:47px;width:235px;height:86px;background:linear-gradient(90deg,#c8865a,#e9b88a 50%,#b6704a)}
.card p{position:absolute;left:8px;top:149px;width:243px;text-align:center;font-size:10px;line-height:14px;color:var(--ink)}
.card .btn{position:absolute;left:68px;top:197px;width:122px;height:28px}

.footer{left:0;top:956px;width:1117px;height:206px;background:linear-gradient(var(--navy),#142a66)}
.footer h3{position:absolute;top:34px;font-size:12px;font-weight:700;letter-spacing:1.3px;color:var(--white)}
.footer .ul{position:absolute;top:51px;height:1px;background:#5468a6}
.footer ul{position:absolute;top:70px;list-style:none}
.footer li{font-size:10.5px;letter-spacing:1.3px;color:var(--footer-text);height:21px}
.footer .contact li{display:flex;gap:10px;align-items:center}
.footer .contact li svg{flex:none}
.footlogo{left:725px;top:37px;width:235px;height:94px;background:var(--white);display:flex;align-items:center;justify-content:center;font-size:16px;font-weight:700;color:var(--navy)}
.social{left:732px;top:150px;display:flex;gap:9px}
.social i{display:block;width:22px;height:22px;border-radius:50%;background:var(--white)}

.bottombar{left:0;top:1162px;width:1117px;height:38px;background:#0e1f4f}
.bottombar p{position:absolute;left:153px;top:14px;font-size:8.5px;letter-spacing:.8px;color:var(--footer-text)}
</style>
</head>
<body>

<div class="abs topbar">
  <div class="abs date">June 12, 2014</div>
  <div class="abs util"><span>SUBMIT QUERY</span><span class="sep">|</span><span>FAQS</span><span class="sep">|</span><span>HELP</span><span class="sep">|</span><span>ARTICLES</span></div>
</div>

<div class="abs masthead"></div>
<div class="abs brand">HAVERFORD &amp; QUIST LLP</div>
<div class="abs callus">Call us <b>800 454 XXXX</b></div>

<div class="abs sky"></div>

<div class="abs hero" role="img" aria-label="City skyline across water under a cloudy sky"></div>
<div class="abs hero-person" role="img" aria-label="Smiling lawyer in a dark suit pointing upward"></div>
<div class="abs arrow" style="left:171px;top:301px"></div>
<div class="abs arrow" style="left:917px;top:301px"></div>

<nav class="abs nav">
  <a class="active" style="width:97px">HOME</a>
  <a style="width:103px">SERVICES</a>
  <a style="width:91px">NEWS</a>
  <a style="width:88px">ABOUT</a>
  <a style="width:108px">CONTACT</a>
  <a style="width:90px">HELP</a>
</nav>
<div class="abs search">
  <svg width="14" height="14" viewBox="0 0 14 14"><circle cx="5.5" cy="5.5" r="4.3" fill="none" stroke="#0d2a7a" stroke-width="1.8"/><line x1="8.8" y1="8.8" x2="13" y2="13" stroke="#0d2a7a" stroke-width="2"/></svg>
</div>

<div class="abs hero-panel">
  <h1>NEED A <b>LAWYER ??</b></h1>
  <div class="rule"></div>
  <p>This is Photoshop's version of Lorem Ipsum. Proin gravida nibh vel velit auctor aliquet.</p>
  <div class="btn blue">KNOW MORE</div>
</div>

<div class="abs about-h">ABOUT <b>HAVERFORD &amp; QUIST LLP</b></div>
<p class="abs about-p" style="top:535px">This is Photoshop's version of Lorem Ipsum. Proin gravida nibh vel velit auctor aliquet. Aenean sollicitudin, lorem quis bibendum auctor, nisi elit consequat ipsum, nec sagittis sem nibh id elit. Duis sed odio sit amet nibh vulputate cursus a sit amet mauris. Morbi accumsan ipsum velit.</p>
<p class="abs about-p" style="top:598px">&nbsp;Nam nec tellus a odio tincidunt auctor a ornare odio. Sed non mauris vitae erat consequat auctor eu in elit. Class aptent taciti sociosqu ad litora torquent per conubia nostra, per inceptos himenaeos.</p>
<div class="abs know">Know more &gt;&gt;</div>

<div class="abs cases">
  <h2>CASE <span>STUDIES</span></h2>
  <div class="rule"></div>
  <p style="top:50px">This is Photoshop's version of Lorem Ipsum. Proin gravida nibh vel velit auctor aliquet.</p>
  <p style="top:91px">Aenean sollicitudin, lorem quis bibendum auctor, nisi elit consequat ipsum, nec sagittis sem nibh id elit.</p>
  <p style="top:132px">Duis sed odio sit amet nibh vulputate cursus a sit amet</p>
  <div class="track"></div><div class="thumb"></div>
</div>

<div class="abs card" style="left:153px">
  <div class="head blue">SERVICE SPECIFICATION</div>
  <div class="photo" role="img" aria-label="Scales of justice in a courtroom"></div>
  <p>Proin gravida nibh vel velit auctor aliquet. Aenean sollicitudin., lorem quis bibendum auctor, nisi elit consequat ipsum sagittis.</p>
  <div class="btn blue">KNOW MORE</div>
</div>
<div class="abs card" style="left:431px">
  <div class="head dark">SERVICE SPECIFICATION</div>
  <div class="photo" role="img" aria-label="Scales of justice in a courtroom"></div>
  <p>Proin gravida nibh vel velit auctor aliquet. Aenean sollicitudin., lorem quis bibendum auctor, nisi elit consequat ipsum sagittis.</p>
  <div class="btn dark">KNOW MORE</div>
</div>
<div class="abs card" style="left:707px">
  <div class="head dark">SERVICE SPECIFICATION</div>
  <div class="photo" role="img" aria-label="Scales of justice in a courtroom"></div>
  <p>Proin gravida nibh vel velit auctor aliquet. Aenean sollicitudin., lorem quis bibendum auctor, nisi elit consequat ipsum sagittis.</p>
  <div class="btn dark">KNOW MORE</div>
</div>

<footer class="abs footer">
  <h3 style="left:153px">QUICK LINKS</h3><div class="ul" style="left:153px;width:122px"></div>
  <ul style="left:153px"><li>HOME</li><li>SERVICES</li><li>NEWS</li><li>ABOUT</li><li>HELP</li></ul>

  <h3 style="left:290px">POPULAR LINKS</h3><div class="ul" style="left:290px;width:124px"></div>
  <ul style="left:290px"><li>CASE STUDIES</li><li>OUR PROMISES</li><li>HOW WE WORK</li><li>OUR VISION</li></ul>

  <h3 style="left:431px">CONTACT DETAILS</h3><div class="ul" style="left:431px;width:260px"></div>
  <ul class="contact" style="left:442px">
    <li><svg width="10" height="12" viewBox="0 0 10 12"><path d="M5 0a4 4 0 0 1 4 4c0 3-4 8-4 8S1 7 1 4a4 4 0 0 1 4-4z" fill="#fff"/><circle cx="5" cy="4" r="1.5" fill="#0d2a7a"/></svg>ADDRESS - XYX TOWER, LOREM IPSUM</li>
    <li style="padding-left:20px">COMPLEX, NEX DUSTER, NEW YORK</li>
    <li><svg width="10" height="12" viewBox="0 0 10 12"><path d="M2 0l2 3-1 1.5c.8 1.8 1.8 2.8 3.5 3.5L8 7l2 2-1.5 2.5C4 11 0 6 .3 1.5z" fill="#fff"/></svg>1800 454 XXXX</li>
    <li><svg width="10" height="12" viewBox="0 0 10 12"><rect x="2" y="1" width="6" height="3" fill="#fff"/><rect x="0" y="4" width="10" height="5" fill="#fff"/><rect x="2" y="8" width="6" height="3" fill="#fff"/></svg>1800 454 XXXX</li>
    <li style="letter-spacing:.9px;text-transform:none"><svg width="10" height="12" viewBox="0 0 10 12"><rect x="0" y="2.5" width="10" height="7" fill="#fff"/><path d="M0 2.5l5 4 5-4" fill="none" stroke="#0d2a7a"/></svg>info@haverfordquist.com</li>
  </ul>

  <div class="abs footlogo">HAVERFORD &amp; QUIST LLP</div>
  <div class="abs social"><i></i><i></i><i></i><i></i><i></i><i></i></div>
</footer>

<div class="abs bottombar"><p>Copyright haverford&amp;quist &nbsp;&nbsp;| &nbsp;&nbsp;2014 &nbsp;&nbsp;| &nbsp;&nbsp;Terms &amp; conditions &nbsp;&nbsp;| &nbsp;&nbsp;Privacy Policy</p></div>

</body>
</html>
```